Marta Business Card

My wife is going to start her own business with renting holiday appartments to tourists. She needs a design for a new business card... and a new web site.
Look at Stayvolt "Erholung auf dem Lindenwäldchen"

Target Market(s)

Give business card to prospects at any situation

Contact Information for Business Card

not sure what this means

Font styles to use
Script

Colors
fec41a
fee18a

Requirements
Must have
• My wife's handwriting is difficult to read:
Entspannen - Loslassen - Auftanken
Marta & das Lindenwäldchen
Urlaub an einem besonderen Ort
Marta Brecke
Grauer Pfad 7
18471 Alt Feldow
post@marta-brecke.de
www.lindenwaeldchen.net
Nice to have
• Beige background
Font like handwriting

```html
<!DOCTYPE html>
<html lang="de">
<head>
<meta charset="UTF-8">
<title>Marta &amp; das Lindenwäldchen – Visitenkarte</title>
<link rel="stylesheet" href="https://fonts.googleapis.com/css2?family=Allura&family=Jost:wght@400&family=Tinos&display=swap">
<style>
  :root {
    --backdrop: #3a3b3c;
    --card-paper: #e3e5e0;
    --ink: #3a3a3a;
    --gold: #b8951f;
  }
  html, body {
    margin: 0;
    padding: 0;
    width: 1200px;
    height: 1200px;
    overflow: hidden;
    background: var(--backdrop);
  }
  .business-card {
    position: absolute;
    left: 50px;
    top: 287px;
    width: 1100px;
    height: 627px;
    background: var(--card-paper);
    color: var(--ink);
    text-align: center;
  }
  .business-card > * {
    position: absolute;
    left: 0;
    right: 0;
    margin: 0;
    white-space: nowrap;
  }
  .motto {
    top: 88px;
    font-family: "Allura", cursive;
    font-size: 64px;
    line-height: 1;
    font-weight: 400;
  }
  .brand-name {
    top: 262px;
    font-family: "Allura", cursive;
    font-size: 80px;
    line-height: 1;
    font-weight: 400;
    color: var(--gold);
  }
  .brand-claim {
    top: 346px;
    font-family: "Tinos", serif;
    font-size: 27px;
    line-height: 1;
    color: var(--gold);
  }
  .contact-line {
    top: 482px;
    font-family: "Jost", sans-serif;
    font-size: 24px;
    line-height: 1;
  }
  .website {
    top: 522px;
    font-family: "Jost", sans-serif;
    font-size: 28px;
    line-height: 1;
    letter-spacing: 2px;
  }
</style>
</head>
<body>
  <section class="business-card">
    <p class="motto">Entspannen - Loslassen - Auftanken</p>
    <h1 class="brand-name">Marta &amp; das Lindenwäldchen</h1>
    <p class="brand-claim">Urlaub an einem besonderen Ort</p>
    <p class="contact-line">Marta Brecke, Grauer Pfad 7, 18471 Alt Feldow | post@marta-brecke.de</p>
    <p class="website">WWW.LINDENWAELDCHEN.NET</p>
  </section>
</body>
</html>
```